College Admissions Consulting needs a small street facing sign for new office location.

I need a graphic design to be used inside window for a banner/sign in office location on a high walking traffic city street, for my company, Campus Compass. I work with high school students and families on the college planning and selection application process. Please check out the website to learn more about what I do (www.myfernleaprep.com). The banner will be used to market our services at our office location. The final design should utilize logo colors, phone number, and website/email information. I'd like to incorporate a my picture in someway because of face recognition. To be printed on a posterboard or vinyl banner.

Target Market(s)

Parents of high school aged children.

Industry/Entity Type

Education

Font styles to use
Sans Serif

Colors
abd037

Requirements
Must have
• Clean, attractive, and professional design. Attract the attention of people walking by. Information must be clear and readable (phone/email, etc.).
Nice to have
• Utilize the picture with crossed arms (without the brown background on picture).
Emphasize tagline:
Mastering The College Admission Process
....with personalized, professional guidance in planning, selecting, and applying to the right colleges.

```html
<!DOCTYPE html>
<html lang="en">
<head>
<meta charset="utf-8">
<title>Campus Compass – Window Banner</title>
<link rel="stylesheet" href="https://fonts.googleapis.com/css2?family=Raleway:ital,wght@0,600;0,700;1,600&family=Arimo:wght@700&display=swap">
<style>
  :root {
    --brand-green: #8cc63f;
    --brand-green-light: #abd037;
    --ink: #4a4a4c;
    --ink-soft: #545456;
    --band: #58585a;
    --band-edge: #a3a3a5;
    --paper: #ffffff;
  }
  * { margin: 0; padding: 0; box-sizing: border-box; }
  html, body { width: 1200px; height: 800px; overflow: hidden; background: var(--paper); }
  .banner { position: relative; width: 1200px; height: 800px; overflow: hidden; background: var(--paper); font-family: "Raleway", sans-serif; }

  .backdrop { position: absolute; inset: 0; }

  .headline { position: absolute; left: 62px; top: 64px; width: 560px; line-height: 1; letter-spacing: -1.5px; }
  .headline__lead { display: block; color: var(--brand-green); font-weight: 700; font-size: 50px; }
  .headline__main { display: block; color: var(--ink); font-weight: 700; font-size: 64px; margin-top: 6px; letter-spacing: -2.5px; }
  .headline__tail { display: block; color: var(--brand-green); font-weight: 700; font-size: 50px; text-align: right; margin-top: 4px; }

  .tagline { position: absolute; left: 64px; top: 280px; width: 520px; color: var(--ink-soft); font-style: italic; font-weight: 600; font-size: 29px; line-height: 40px; letter-spacing: -0.6px; }

  .brand { position: absolute; left: 100px; top: 446px; display: flex; align-items: center; gap: 18px; }
  .brand__dot { width: 66px; height: 66px; border-radius: 50%; background: var(--brand-green); flex: none; }
  .brand__text { display: flex; flex-direction: column; }
  .brand__name { color: var(--ink); font-weight: 600; font-size: 44px; line-height: 1; letter-spacing: -0.5px; }
  .brand__motto { color: var(--ink); font-weight: 600; font-size: 13px; letter-spacing: 0.6px; margin-top: 10px; text-transform: uppercase; }

  .phone { position: absolute; left: 86px; top: 560px; font-family: "Arimo", sans-serif; font-weight: 700; white-space: nowrap; }
  .phone__label { color: var(--brand-green); font-size: 44px; }
  .phone__number { color: var(--ink); font-size: 62px; letter-spacing: -0.5px; }

  .contact-band { position: absolute; left: 0; top: 676px; width: 1200px; height: 124px; background: var(--band); border-top: 6px solid var(--band-edge); display: flex; align-items: center; justify-content: center; }
  .contact-band__email { color: var(--paper); font-family: "Arimo", sans-serif; font-weight: 700; font-size: 66px; letter-spacing: -0.5px; text-shadow: 3px 3px 3px rgba(0,0,0,0.55); }
</style>
</head>
<body>
<main class="banner">
  <svg class="backdrop" width="1200" height="800" viewBox="0 0 1200 800" aria-hidden="false">
    <defs>
      <radialGradient id="circleFill" cx="0.55" cy="0.45" r="0.6">
        <stop offset="0" stop-color="#a9d65e"/>
        <stop offset="1" stop-color="#8cc63f"/>
      </radialGradient>
      <clipPath id="circleClip"><circle cx="1050" cy="420" r="428"/></clipPath>
      <linearGradient id="portraitTone" x1="0" y1="0" x2="0" y2="1">
        <stop offset="0" stop-color="#3b2c25"/>
        <stop offset="0.45" stop-color="#b58a73"/>
        <stop offset="0.6" stop-color="#1e1e1e"/>
        <stop offset="1" stop-color="#141414"/>
      </linearGradient>
    </defs>
    <circle class="hero-circle__rim" cx="1050" cy="420" r="434" fill="#9fd052"/>
    <circle class="hero-circle" cx="1050" cy="420" r="428" fill="url(#circleFill)"/>
    <g class="hero-circle__bubbles" clip-path="url(#circleClip)" fill="#ffffff">
      <circle cx="760" cy="70" r="90" opacity="0.18"/>
      <circle cx="885" cy="340" r="120" opacity="0.16"/>
      <circle cx="720" cy="468" r="45" opacity="0.2"/>
      <circle cx="1165" cy="58" r="50" opacity="0.2"/>
      <circle cx="1148" cy="355" r="36" opacity="0.2"/>
    </g>
    <rect class="portrait" x="730" y="10" width="430" height="666" rx="160" ry="160" fill="url(#portraitTone)" role="img" aria-label="Portrait photo of the consultant smiling with arms crossed"/>
  </svg>

  <h1 class="headline">
    <span class="headline__lead">Mastering The</span>
    <span class="headline__main">College Admission</span>
    <span class="headline__tail">Process</span>
  </h1>

  <p class="tagline">....with personalized, professional guidance in planning, selecting, and applying to the right colleges.</p>

  <div class="brand">
    <span class="brand__dot"></span>
    <div class="brand__text">
      <span class="brand__name">Campus Compass</span>
      <span class="brand__motto">Mastering the College Admission Process</span>
    </div>
  </div>

  <p class="phone"><span class="phone__label">Call: </span><span class="phone__number">100 555 010</span></p>

  <footer class="contact-band">
    <span class="contact-band__email">info@myfernleaprep.com</span>
  </footer>
</main>
</body>
</html>
```